Morning Harbor Bible Fellowship needs a new Business Card/Letterhead Suite

***** IT DOES NOT HAVE TO FEATURE GREEN AND BROWN in order to be a successful design*****

****FONTS: SF New Republic, 'Morning Harbor'; Nexa Light, 'Bible Fellowship'****

***We have two locations, with two addresses. So the business card AND letterhead need to include two sets of address information***

We are a growing church in New York in need of a new stationary suite. We have recently adopted a new logo (via a successful ArtHivePro project) and need new business cards, letterhead, envelopes, and folders.

We would like to see creative, original designs that are modern and clean/elegant (NOT dated "churchy" graphics that are cheesy).

We need this project worked on immediately, as we need to print new business cards for upcoming programs we have on our schedule. So, the designs need to be solid so that we can move quickly throughout the revision process toward print.

We'd also need editables files, so that we can drop in other staff members names/phone numbers, to be able to print cards for those staff needing them.

Requirements
Must have
• Our logo
• Must be given to us in an editable format (to change names)
Nice to have
• Some examples on grey, or recycled, card stock
• card stock (background) does not have to be white
Should not have
• Any extraneous logo's or symbols

```html
<!DOCTYPE html>
<html lang="en">
<head>
<meta charset="utf-8">
<title>Morning Harbor Bible Fellowship — Stationery Suite</title>
<link rel="stylesheet" href="https://fonts.googleapis.com/css2?family=Questrial&display=swap">
<style>
  :root{
    --bg:#e7e7e7;
    --paper:#f3f3f3;
    --green:#2f7a22;
    --brown:#6b5c24;
    --ink:#2b2b2b;
    --black:#050505;
    --rule:#c9cfc3;
  }
  *{box-sizing:border-box;margin:0;padding:0}
  html,body{width:1200px;height:900px;overflow:hidden;background:var(--bg)}
  body{position:relative;font-family:'Questrial',sans-serif;color:var(--ink)}

  .sheet{position:absolute;background:var(--paper);box-shadow:0 1px 3px rgba(0,0,0,.12);overflow:hidden}

  .wordmark{color:var(--green);text-align:center;line-height:1;font-weight:400}
  .wordmark .name{display:block;letter-spacing:-.02em;white-space:nowrap}
  .wordmark .sub{display:block;text-transform:uppercase;color:var(--brown);white-space:nowrap}

  .stripe{position:absolute;height:3px;background:linear-gradient(90deg,var(--green) 0%,var(--green) 45%,var(--brown) 70%,var(--brown) 100%)}
  .contact-line{position:absolute;font-size:5px;line-height:1.45;color:#555;white-space:nowrap;text-align:center}
  .contact-line .sep{color:#999;margin:0 3px}

  /* CD sleeve */
  .cd-sleeve{left:76px;top:104px;width:188px;height:188px}
  .cd-sleeve .notch{position:absolute;right:0;top:62px;width:12px;height:64px;background:var(--bg);border-radius:12px 0 0 12px}
  .cd-sleeve .wordmark{position:absolute;left:0;right:12px;top:86px}
  .cd-sleeve .name{font-size:17px}
  .cd-sleeve .sub{font-size:5px;letter-spacing:.3em;margin-top:3px}

  /* Envelope */
  .envelope-back{left:324px;top:102px;width:334px;height:166px}
  .envelope-back svg{position:absolute;left:0;top:0}
  .envelope-back .band{position:absolute;left:0;bottom:0;width:100%;height:3px;background:var(--green)}
  .envelope-front{left:402px;top:133px;width:332px;height:166px}
  .envelope-front .wordmark{position:absolute;right:22px;top:24px;text-align:right}
  .envelope-front .name{font-size:18px}
  .envelope-front .sub{font-size:5px;letter-spacing:.3em;margin-top:3px}
  .envelope-front .contact-line{left:14px;right:14px;bottom:8px;font-size:4.6px}
  .envelope-front .stripe{left:0;right:0;bottom:0}

  /* Folder */
  .folder{left:75px;top:350px;width:315px;height:446px}
  .folder .wordmark{position:absolute;left:0;right:0;top:205px}
  .folder .name{font-size:29px}
  .folder .sub{font-size:8px;letter-spacing:.32em;margin-top:6px}

  /* Letterhead */
  .letterhead{left:421px;top:350px;width:315px;height:446px}
  .letterhead .header-rule{position:absolute;left:34px;right:30px;top:55px;height:1px;background:var(--rule)}
  .letterhead .header{position:absolute;left:34px;right:30px;top:34px;text-align:center}
  .letterhead .header .wordmark{display:inline-block;background:var(--paper);position:relative;padding:0 8px}
  .letterhead .header .name{font-size:20px}
  .letterhead .header .sub{font-size:6px;letter-spacing:.32em;margin-top:4px}
  .letter-body{position:absolute;left:42px;right:38px;top:83px;font-size:5.4px;line-height:1.38;color:#333}
  .letter-body p{margin-bottom:7px}
  .letter-body .gap{margin-bottom:22px}
  .letterhead .contact-line{left:24px;right:24px;bottom:17px}
  .letterhead .stripe{left:24px;right:24px;bottom:12px;height:2px}

  /* Black folder */
  .black-folder{left:778px;top:104px;width:346px;height:472px;background:var(--black)}
  .black-folder .wordmark{position:absolute;right:30px;top:358px}
  .black-folder .name{font-size:28px}
  .black-folder .sub{font-size:8px;letter-spacing:.32em;margin-top:6px;color:#4a4220}

  /* Business cards */
  .card{width:137px;height:78px}
  .card-front{left:839px;top:716px}
  .card-front .wordmark{position:absolute;left:0;right:0;top:28px}
  .card-front .name{font-size:14px}
  .card-front .sub{font-size:4px;letter-spacing:.3em;margin-top:3px}
  .card-back{left:988px;top:716px;background:var(--black);color:#fff}
  .card-back .wordmark{position:absolute;right:10px;top:10px;text-align:right}
  .card-back .name{font-size:9px}
  .card-back .sub{font-size:2.6px;letter-spacing:.3em;margin-top:2px;color:#4a4220}
  .card-back .person{position:absolute;left:12px;top:26px;font-size:5.4px;line-height:1.3}
  .card-back .person small{display:block;font-size:3.4px;color:#ddd;line-height:1.45}
  .card-back .details{position:absolute;left:12px;right:10px;top:58px;display:flex;justify-content:space-between;font-size:3.2px;line-height:1.5;color:#ddd}
</style>
</head>
<body>

  <section class="sheet cd-sleeve" aria-label="CD sleeve">
    <div class="notch"></div>
    <div class="wordmark"><span class="name">Morning Harbor</span><span class="sub">Bible Fellowship</span></div>
  </section>

  <section class="sheet envelope-back" aria-label="Envelope back">
    <svg width="334" height="166" viewBox="0 0 334 166">
      <polygon points="0,0 334,0 334,6 310,54 24,54 0,6" fill="#e9e9e9" stroke="#d2d2d2" stroke-width="1"/>
    </svg>
    <div class="band"></div>
  </section>

  <section class="sheet envelope-front" aria-label="Envelope">
    <div class="wordmark"><span class="name">Morning Harbor</span><span class="sub">Bible Fellowship</span></div>
    <div class="contact-line">
      210 Harbor View Road, Oyster Bay NY 11771<span class="sep">|</span>88 Cedar Lane, Glen Cove NY 11542<span class="sep">|</span>+1 516 555 0142<span class="sep">|</span>office@morningharbor.org
    </div>
    <div class="stripe"></div>
  </section>

  <section class="sheet folder" aria-label="Presentation folder">
    <div class="wordmark"><span class="name">Morning Harbor</span><span class="sub">Bible Fellowship</span></div>
  </section>

  <section class="sheet letterhead" aria-label="Letterhead">
    <div class="header-rule"></div>
    <div class="header">
      <div class="wordmark"><span class="name">Morning Harbor</span><span class="sub">Bible Fellowship</span></div>
    </div>
    <div class="letter-body">
      <p>14 Quay Street<br>Oyster Bay, NY 11771</p>
      <p>January 29th, 2011</p>
      <p>Mr. Whitfield<br>President, Whitfield Youth Center<br>58 Elm Court<br>New York, NY 10025</p>
      <p>Dear Mr. Whitfield:</p>
      <p class="gap">In the first paragraph, one needs to give a brief introduction of oneself. One should also give reference to the purpose of the letter in brief. The second paragraph needs to give the details of the letter and its need. This paragraph is mostly longer than the others and plays the main role in the letter. Keep the sentences short and to the point. Avoid using complex words and sentences.</p>
      <p>The third and last paragraph is the conclusion of the letter and can be kept short.</p>
      <p>Sincerely,</p>
      <p>(this is where the signature of the writer will be placed)</p>
      <p>Daniel Reyes<br>Read more at Letter Guide: http://www.letterguide.example/format</p>
    </div>
    <div class="contact-line">
      Oyster Bay: 210 Harbor View Road, Oyster Bay NY 11771<span class="sep">|</span>+1 516 555 0142<br>
      Glen Cove: 88 Cedar Lane, Glen Cove NY 11542<span class="sep">|</span>+1 516 555 0198<span class="sep">|</span>office@morningharbor.org<span class="sep">|</span>morningharbor.org
    </div>
    <div class="stripe"></div>
  </section>

  <section class="sheet black-folder" aria-label="Black folder cover">
    <div class="wordmark"><span class="name">Morning Harbor</span><span class="sub">Bible Fellowship</span></div>
  </section>

  <section class="sheet card card-front" aria-label="Business card front">
    <div class="wordmark"><span class="name">Morning Harbor</span><span class="sub">Bible Fellowship</span></div>
  </section>

  <section class="sheet card card-back" aria-label="Business card back">
    <div class="wordmark"><span class="name">Morning Harbor</span><span class="sub">Bible Fellowship</span></div>
    <div class="person">Daniel Reyes
      <small>Pastor</small>
      <small>210 Harbor View Road, Oyster Bay NY 11771</small>
      <small>88 Cedar Lane, Glen Cove NY 11542</small>
    </div>
    <div class="details">
      <span>+1 516 555 0142<br>+1 516 555 0198</span>
      <span>office@morningharbor.org<br>morningharbor.org</span>
    </div>
  </section>

</body>
</html>
```